Need a solid log.
My company Sales: OrbiCast, Halcyon Beam, Vorlan Internet
Design and installation of WI_FI systems.
Fulfillment company for installations in the Electronics industry

Industry/Entity Type

Electronics

Contact Information for Business Card

Peter R. Hollowell
President
Phone: 479.555.0182 Cell: 479.5550947 prhollowell@brightharbornet.biz
Bright Harbor Networks
Larkton, AL. 35999

```html
<!DOCTYPE html>
<html lang="en">
<head>
<meta charset="utf-8">
<title>Bright Harbor Networks – Business Card</title>
<link rel="stylesheet" href="https://fonts.googleapis.com/css2?family=Source+Sans+3:wght@400;600;700&display=swap">
<style>
  :root {
    --page-bg: #e6e8eb;
    --card-blue: #5bc9ef;
    --band-white: #ffffff;
    --rule-dark: #3a3a3a;
    --text-white: #ffffff;
    --name-blue: #4fc0ea;
    --divider: #4a4a4a;
  }
  * { margin: 0; padding: 0; box-sizing: border-box; }
  html, body {
    width: 1200px;
    height: 960px;
    overflow: hidden;
    background: var(--page-bg);
    font-family: "Source Sans 3", Arial, sans-serif;
  }
  .card {
    position: absolute;
    left: 100px;
    top: 187px;
    width: 1000px;
    height: 585px;
    background: var(--card-blue);
    overflow: hidden;
  }
  .brand-name {
    position: absolute;
    top: 98px;
    left: 0;
    width: 100%;
    text-align: center;
    font-size: 70px;
    font-weight: 700;
    line-height: 1;
    color: var(--text-white);
  }
  .brand-rule {
    position: absolute;
    top: 183px;
    left: 72px;
    width: 832px;
    height: 6px;
    background: var(--rule-dark);
  }
  .services {
    position: absolute;
    top: 202px;
    left: 0;
    width: 100%;
    display: flex;
    justify-content: center;
    align-items: center;
    list-style: none;
    font-size: 32px;
    line-height: 40px;
    color: var(--text-white);
  }
  .services li { padding: 0 26px; }
  .services li + li { border-left: 4px solid var(--divider); }
  .name-band {
    position: absolute;
    top: 256px;
    left: 0;
    width: 100%;
    height: 150px;
    background: var(--band-white);
    box-shadow: 0 -10px 14px rgba(0,0,0,0.18), 0 10px 14px rgba(0,0,0,0.22);
    text-align: center;
  }
  .person-name {
    padding-top: 32px;
    font-size: 72px;
    font-weight: 400;
    line-height: 1;
    color: var(--name-blue);
  }
  .person-title {
    margin-top: 4px;
    font-size: 29px;
    line-height: 1;
    color: var(--name-blue);
  }
  .contact {
    position: absolute;
    top: 425px;
    left: 0;
    width: 100%;
    text-align: center;
    font-size: 27px;
    line-height: 37px;
    color: var(--text-white);
    font-style: normal;
  }
</style>
</head>
<body>
  <main class="card">
    <h1 class="brand-name">Bright Harbor Networks</h1>
    <div class="brand-rule"></div>
    <ul class="services">
      <li>OrbiCast</li>
      <li>Halcyon Beam</li>
      <li>Vorlan Internet</li>
      <li>WI Fi systems</li>
    </ul>
    <section class="name-band">
      <h2 class="person-name">Peter R. Hollowell</h2>
      <p class="person-title">President</p>
    </section>
    <address class="contact">
      <p>Phone: 479.555.0182,&nbsp;&nbsp; Cell: 479.5550947</p>
      <p>prhollowell@brightharbornet.biz</p>
      <p>Bright Harbor Networks Larkton, AL. 35999</p>
    </address>
  </main>
</body>
</html>
```